Bref créative
Business Cards/Letterhead for a Private Equity Real Estate Company
KTR Commercial
Simple
H. Dalton Greave
President
4780 Brambling Road
Suite 610
Atlanta, GA 30342
dalton@ktrcommercial.net
http://ktrcommercial.net/
We think we want the logo on one side and then all the written information on the other. Open to seeing different suggestions, though. Thanks for everyone who participates!

```html
<!DOCTYPE html>
<html lang="en">
<head>
<meta charset="utf-8">
<title>KTR Commercial — Business Card</title>
<link href="https://fonts.googleapis.com/css2?family=Open+Sans:wght@400;600&display=swap" rel="stylesheet">
<style>
  :root {
    --backdrop: #e6e7e9;
    --card-dark-1: #2a2b2d;
    --card-dark-2: #6d6e71;
    --card-light-1: #ffffff;
    --card-light-2: #dcdddf;
    --band-1: #5c5d60;
    --band-2: #a7a8ab;
    --ink: #3d3e40;
    --ink-soft: #6a6b6e;
    --accent: #b3242a;
    --silver: #d9dadc;
    --rule: #b8b9bb;
  }
  * { margin: 0; padding: 0; box-sizing: border-box; }
  html, body { width: 1200px; height: 901px; overflow: hidden; }
  body {
    background: var(--backdrop);
    display: flex;
    flex-direction: column;
    align-items: center;
    justify-content: center;
    gap: 48px;
    font-family: "Open Sans", Arial, sans-serif;
  }
  .card {
    width: 660px;
    height: 377px;
    position: relative;
    overflow: hidden;
    box-shadow: 0 6px 18px rgba(0,0,0,.18);
  }
  .brand-name {
    font-family: "Open Sans", Arial, sans-serif;
    font-weight: 600;
    line-height: 1;
    white-space: nowrap;
  }

  /* Back side */
  .card--back {
    background: linear-gradient(135deg, var(--card-dark-1) 0%, var(--card-dark-2) 55%, var(--card-dark-1) 100%);
    display: flex;
    flex-direction: column;
    align-items: center;
    justify-content: center;
  }
  .card--back .brand-name { font-size: 42px; color: var(--silver); }
  .card--back .brand-web { font-size: 13px; margin-top: 16px; letter-spacing: 1px; color: var(--silver); }

  /* Front side */
  .card--front {
    background: linear-gradient(160deg, var(--card-light-1) 0%, var(--card-light-2) 100%);
    color: var(--ink);
  }
  .front-band {
    position: absolute;
    left: 0; right: 0;
    top: 58px; height: 62px;
    background: linear-gradient(180deg, var(--band-2) 0%, var(--band-1) 50%, var(--band-2) 100%);
  }
  .front-brand {
    position: absolute;
    left: 50%; top: 50px;
    transform: translateX(-50%);
    width: 290px;
    height: 78px;
    background: var(--card-light-1);
    display: flex;
    align-items: center;
    justify-content: center;
  }
  .front-brand .brand-name { font-size: 30px; color: var(--ink); }
  .person {
    position: absolute;
    top: 158px; left: 0; right: 0;
    text-align: center;
  }
  .person-name { color: var(--accent); font-weight: 600; font-size: 17px; line-height: 1.3; }
  .person-title { color: var(--ink-soft); font-size: 13px; margin-top: 2px; }
  .contact {
    position: absolute;
    top: 246px; left: 0; right: 0;
    display: flex;
    justify-content: center;
    font-size: 13px;
    line-height: 21px;
    color: var(--ink);
  }
  .contact-address { text-align: right; padding-right: 18px; width: 200px; font-style: normal; }
  .contact-divider { width: 1px; background: var(--rule); }
  .contact-lines { padding-left: 14px; list-style: none; }
  .contact-lines li { display: flex; align-items: center; gap: 10px; }
  .contact-lines svg { width: 13px; height: 13px; fill: var(--accent); flex: none; }
</style>
</head>
<body>

<section class="card card--back" aria-label="Card back">
  <div class="brand-name">KTR Commercial</div>
  <div class="brand-web">ktrcommercial.net</div>
</section>

<section class="card card--front" aria-label="Card front">
  <div class="front-band"></div>
  <div class="front-brand">
    <div class="brand-name">KTR Commercial</div>
  </div>

  <div class="person">
    <div class="person-name">H. Dalton Greave</div>
    <div class="person-title">President</div>
  </div>

  <div class="contact">
    <address class="contact-address">
      4780 Brambling Road<br>
      Suite 610<br>
      Atlanta, GA 30342
    </address>
    <div class="contact-divider"></div>
    <ul class="contact-lines">
      <li>
        <svg viewBox="0 0 16 16" aria-hidden="true"><path d="M3 1h3l1 4-2 1a9 9 0 0 0 5 5l1-2 4 1v3a2 2 0 0 1-2 2A13 13 0 0 1 1 3a2 2 0 0 1 2-2z"/></svg>
        (404) 555-0148
      </li>
      <li>
        <svg viewBox="0 0 16 16" aria-hidden="true"><path d="M4 0h8a1 1 0 0 1 1 1v14a1 1 0 0 1-1 1H4a1 1 0 0 1-1-1V1a1 1 0 0 1 1-1zm1 2v10h6V2zm3 11a1 1 0 1 0 0 2 1 1 0 0 0 0-2z"/></svg>
        (404) 555-0172
      </li>
      <li>
        <svg viewBox="0 0 16 16" aria-hidden="true"><path d="M0 3h16v10H0zm1.5 1L8 9l6.5-5z"/></svg>
        dalton@ktrcommercial.net
      </li>
      <li>
        <svg viewBox="0 0 16 16" aria-hidden="true"><path d="M8 0a8 8 0 1 0 0 16A8 8 0 0 0 8 0zm0 1.5c.9 0 2 1.7 2.4 5H5.6C6 3.2 7.1 1.5 8 1.5zm-2.4 6.5h4.8c-.4 3.300-1.5 6.5-2.4 6.5S6 11.3 5.6 8zM1.6 8h2.5c.1 2 .5 3.7 1.1 5A6.5 6.5 0 0 1 1.6 8zm10.3 0h2.5a6.5 6.5 0 0 1-3.6 5c.6-1.3 1-3 1.1-5zM1.6 6.5A6.5 6.5 0 0 1 5.2 3c-.6 1.1-1 2.3-1.1 3.5zm10.3 0c-.1-1.2-.5-2.4-1.1-3.5a6.5 6.5 0 0 1 3.6 3.5z"/></svg>
        www.ktrcommercial.net
      </li>
    </ul>
  </div>
</section>

</body>
</html>
```